We are a printed circuit board manufacturer. Need a company professional web site to allow our potential customers to know more about our background, capability and our products. The web site will contain three languages, which are Chinese, English and Japanese. Our audience are mainly electronic companies that procure printed circuit boards. I have a word document that have all the required text in all three languages. The final design should communicate the impression that we embrace quality, trustworthiness and long term partnership business principles.
We should have sections that allow us to post pictures of our facilities.
I have added the three files in three different languages.
Some of the information is below:
Background
RVD Worldwide Limited (RVD) was set up in Hong Kong in 2007 by two Hong Kong entrepreneurs, Mr. Lok Fai Tam and Mr. Wai Ho. We acquired the single sided printed circuit board factory located in Dongguan City, Guangdong Province, China, from Valtor Corporation of the U.S. in 2007. In addition to RVD, Mr. Tam and Mr. Ho also own Brightrail Systems Company Limited, a semiconductor company based in Hong Kong since 1997 with a total investment of over US$100 million. Brightrail is engaged in the manufacturing of flexible substrates and MEMS assembly business.
RVD has been awarded TS 16949 and ISO14000 certificates since 2009 and 2004 respectively.
Business Principles
RVD Worldwide Limited strives to be a professional top notched printed circuit board supplier. We embrace four “EXCELLENCE” principles, namely, excellence in quality, excellence in prices, excellence in services and excellence in on time delivery.
We approach each customer with a long-term partnership view that delivers the lowest ownership costs and highest total values to our customers. We customize quotations and solutions in order to allow our customers to win more businesses. We believe by thinking from our customers’ points of view we will be able to create a WIN-WIN relationship.
Customers
Due to our excellent quality, services and production systems, RVD Worldwide Limited manage to service a number of large Japanese and US customers, which include:
Technical capability overview
Below is an overview of our current capability:
Target Market(s)
Electronic companies buyers
Industry/Entity Type
Business
Requirements
Must have
- Capability description
Should not have
- no cartoon

```html
<!DOCTYPE html>
<html lang="en">
<head>
<meta charset="utf-8">
<title>RVD Worldwide Limited</title>
<link href="https://fonts.googleapis.com/css2?family=Kreon:wght@300;400;600&family=Open+Sans:wght@400;600;700&display=swap" rel="stylesheet">
<style>
:root{
  --teal:#13836a;
  --brand:#1d7a52;
  --white:#ffffff;
  --light:#efefef;
  --hero:#333644;
  --dark:#333333;
  --black:#000000;
  --ink:#2b2b2b;
  --heading-dark:#333333;
  --rule:#c8c8c8;
  --field:#acacac;
}
*{box-sizing:border-box;margin:0;padding:0}
html,body{width:1172px;height:1200px;overflow:hidden}
body{position:relative;background:var(--white);font-family:"Open Sans",Arial,sans-serif;color:var(--ink)}
.abs{position:absolute}

/* header */
.site-header{left:0;top:0;width:1172px;height:130px;background:var(--white)}
.brand{left:150px;top:28px;color:var(--brand);font-family:"Kreon",serif;font-weight:600;line-height:1}
.brand .brand-main{display:block;font-size:48px;letter-spacing:8px}
.brand .brand-sub{display:block;font-size:19px;letter-spacing:1px;margin-top:4px;padding-left:10px}
.lang{top:25px;width:33px;height:33px;border-radius:50%;border:1px solid #d6d6d6}
.lang-zh{left:877px;background:radial-gradient(circle at 40% 35%,#e8352a,#b81d17)}
.lang-en{left:919px;background:radial-gradient(circle at 40% 35%,#3a5aa8,#1f3a80)}
.lang-ja{left:964px;background:var(--white)}
.lang-ja::after{content:"";position:absolute;left:9px;top:9px;width:13px;height:13px;border-radius:50%;background:#d21f2a}
.phone{right:176px;top:68px;font-family:Arial,sans-serif;font-size:16px;color:#444}
.main-nav{top:107px;font-family:"Kreon",serif;font-size:15px;color:#333}
.main-nav a{position:absolute;color:inherit;text-decoration:none;white-space:nowrap}

/* hero */
.hero{left:0;top:130px;width:1172px;height:293px;background:var(--hero)}
.hero-photo{left:139px;top:130px;width:859px;height:293px;background:linear-gradient(160deg,#b9b5a8 0%,#d9d9d6 40%,#c4c7c6 70%,#8a8c86 100%);box-shadow:3px 3px 6px rgba(0,0,0,.6)}

/* light section */
.about{left:0;top:423px;width:1172px;height:391px;background:var(--light)}
.section-title{font-family:"Kreon",serif;font-weight:300;font-size:26px;line-height:1;display:flex;align-items:center;white-space:nowrap}
.section-title::before{content:"";width:14px;height:14px;border-radius:50%;background:var(--teal);margin-right:6px}
.title-on-light{color:var(--heading-dark)}
.title-on-dark{color:var(--white)}
.customers-title{left:113px;top:435px}
.background-title{left:566px;top:435px}

.customer-table{left:106px;top:483px;width:424px}
.row{display:flex;border-bottom:1px solid var(--rule)}
.row:last-child{border-bottom:none}
.row .sector{width:72px;flex:none;text-align:center;font-size:9.5px;font-weight:600;line-height:1.25;color:#333;border-right:1px solid var(--rule);display:flex;align-items:center;justify-content:center}
.row .names{flex:1;position:relative}
.client{position:absolute;font-family:"Open Sans",sans-serif;color:#2a2a2a;white-space:nowrap;line-height:1}
.divider{left:535px;top:450px;width:2px;height:340px;background:var(--teal)}

.copy{font-size:12.5px;line-height:14.8px}
.background-copy{left:558px;top:483px;width:445px;color:#333}
.copy p+p{margin-top:14.8px}
.btn{display:flex;align-items:center;justify-content:center;background:var(--teal);color:var(--white);font-size:17px;border-radius:5px;text-decoration:none}
.background-btn{left:558px;top:689px;width:122px;height:37px}

/* dark section */
.principles{left:0;top:814px;width:1172px;height:319px;background:var(--dark)}
.principles-title{left:113px;top:820px}
.contact-title{left:566px;top:820px}
.principles-copy{left:116px;top:866px;width:448px;color:var(--white)}
.principles-btn{left:115px;top:1046px;width:121px;height:36px}
.field{left:585px;width:369px;background:var(--field);color:var(--white);font-family:Arial,sans-serif;font-weight:700;font-size:14px;padding:8px 9px}
.field-email{top:864px;height:34px;padding-left:11px}
.field-tel{top:908px;height:34px}
.field-subject{top:953px;height:34px}
.field-message{top:997px;height:118px}

/* footer */
.site-footer{left:0;top:1133px;width:1172px;height:67px;background:var(--black)}
.social{top:1141px;width:32px;height:32px;border-radius:50%;background:#d9d9d9}
.social-1{left:115px}.social-2{left:163px}.social-3{left:210px}
.footer-nav{left:351px;top:1149px;display:flex;align-items:center;font-family:"Kreon",serif;font-size:15px;color:var(--white)}
.footer-nav a{color:inherit;text-decoration:none}
.footer-nav .sep{display:inline-block;width:2px;height:20px;background:var(--white);margin:0 22px}
</style>
</head>
<body>

<header class="site-header abs"></header>
<div class="brand abs"><span class="brand-main">RVD</span><span class="brand-sub">Worldwide Limited</span></div>
<span class="lang lang-zh abs" role="img" aria-label="Chinese language"></span>
<span class="lang lang-en abs" role="img" aria-label="English language"></span>
<span class="lang lang-ja abs" role="img" aria-label="Japanese language"></span>
<div class="phone abs">(02) 555- 01234</div>
<nav class="main-nav abs" style="left:0">
  <a href="#" style="left:548px">Home</a>
  <a href="#" style="left:637px">Products</a>
  <a href="#" style="left:746px">Services</a>
  <a href="#" style="left:851px">About Us</a>
  <a href="#" style="left:945px">Contact</a>
</nav>

<section class="hero abs"></section>
<div class="hero-photo abs" role="img" aria-label="Photo of printed circuit board production machinery in the factory"></div>

<section class="about abs"></section>
<h2 class="section-title title-on-light customers-title abs">Customers</h2>
<div class="customer-table abs">
  <div class="row" style="height:51px">
    <div class="sector">Auto<br>Motive</div>
    <div class="names">
      <span class="client" style="left:42px;top:7px;font-size:18px;font-weight:600">Harlow Industries</span>
      <span class="client" style="left:52px;top:31px;font-size:15px;font-weight:700">Brenner</span>
      <span class="client" style="left:133px;top:33px;font-size:10px;font-weight:700">Kasora Motor</span>
      <span class="client" style="left:282px;top:21px;font-size:10px">Corvane</span>
    </div>
  </div>
  <div class="row" style="height:56px">
    <div class="sector">Video<br>&amp; Audio</div>
    <div class="names">
      <span class="client" style="left:72px;top:19px;font-size:19px;font-weight:700">Fenwa</span>
      <span class="client" style="left:208px;top:19px;font-size:19px;font-weight:700">Sorada</span>
    </div>
  </div>
  <div class="row" style="height:57px">
    <div class="sector">Home<br>Appliances<br>&amp; Camera</div>
    <div class="names">
      <span class="client" style="left:28px;top:8px;font-size:16px;font-weight:700">MIRATO</span>
      <span class="client" style="left:28px;top:33px;font-size:12px;font-weight:600">Xinyan Tech</span>
      <span class="client" style="left:152px;top:16px;font-size:13px;font-weight:700">HOSHIDA</span>
      <span class="client" style="left:236px;top:6px;font-size:19px;font-weight:700">Palmetra</span>
      <span class="client" style="left:258px;top:32px;font-size:17px">Shirano</span>
    </div>
  </div>
  <div class="row" style="height:62px">
    <div class="sector">Industrial<br>Equipment &amp;<br>Power<br>Supplier</div>
    <div class="names">
      <span class="client" style="left:62px;top:20px;font-size:20px;font-weight:700">ARVEC</span>
      <span class="client" style="left:165px;top:17px;font-size:23px;font-weight:600">Dalvorn</span>
    </div>
  </div>
  <div class="row" style="height:52px">
    <div class="sector">Contract<br>Manufacturers</div>
    <div class="names">
      <span class="client" style="left:40px;top:15px;font-size:22px;font-weight:600">Harlow Industries</span>
    </div>
  </div>
</div>
<div class="divider abs"></div>

<h2 class="section-title title-on-light background-title abs">Background</h2>
<div class="copy background-copy abs">
  <p>RVD Worldwide Limited (RVD) was set up in Hong Kong in 2007 by two Hong Kong entrepreneurs, Mr. Lok Fai Tam and Mr. Wai Ho. We acquired the single sided printed circuit board factory located in Dongguan City, Guangdong Province, China, from Valtor Corporation of the U.S. in 2007. In addition to RVD, Mr. Tam and Mr. Ho also own Brightrail Systems Company Limited, a semiconductor company based in Hong Kong since 1997 with a total investment of over US$100 million. Brightrail is engaged in the manufacturing of flexible substrates and MEMS assembly business.</p>
  <p>RVD has been awarded TS 16949 and ISO14000 certificates since 2009 and 2004 respectively.</p>
</div>
<a class="btn background-btn abs" href="#">Learn More</a>

<section class="principles abs"></section>
<h2 class="section-title title-on-dark principles-title abs">Business Principles</h2>
<div class="copy principles-copy abs">
  <p>RVD Worldwide Limited strives to be a professional top notched printed circuit board supplier. We embrace four “EXCELLENCE” principles, namely, excellence in quality, excellence in prices, excellence in services and excellence in on time delivery.</p>
  <p>We approach each customer with a long-term partnership view that delivers the lowest ownership costs and highest total values to our customers. We customize quotations and solutions in order to allow our customers to win more businesses. We believe by thinking from our customers’ points of view we will be able to create a WIN-WIN relationship.</p>
</div>
<a class="btn principles-btn abs" href="#">Learn More</a>

<h2 class="section-title title-on-dark contact-title abs">Contact Us</h2>
<div class="field field-email abs">Email</div>
<div class="field field-tel abs">Tel</div>
<div class="field field-subject abs">Subject</div>
<div class="field field-message abs">Contect</div>

<footer class="site-footer abs"></footer>
<span class="social social-1 abs" role="img" aria-label="Social network link"></span>
<span class="social social-2 abs" role="img" aria-label="Social network link"></span>
<span class="social social-3 abs" role="img" aria-label="Social network link"></span>
<nav class="footer-nav abs">
  <a href="#">Home</a><span class="sep"></span>
  <a href="#">Products</a><span class="sep"></span>
  <a href="#">Services</a><span class="sep"></span>
  <a href="#">About Us</a><span class="sep" style="margin:0 14px 0 6px"></span>
  <a href="#">Contact</a>
</nav>

</body>
</html>
```